Central Florida Lawn and Landscape business needs an awesome flyer design!

We are a growing lawn and landscape maintenance business looking to incorporate print mail for target advertising. This project should provide some editing capabilities for us to incorporate our logo, update any promotional offers, and adjust throughout the various seasons (lawn service, mulch jobs, one-time clean-ups, hardscape projects, etc). We'd like a clear call to action (one that we can edit if needed) to call or text today. We'll include our website address as well.
The business name is Velo Grassworks.
Target Market(s)
Residential homeowners
Industry/Entity Type
Lawn and landscape maintenance
Font styles to use
Other font styles liked:
- Couture
Look and feel

```html
<!DOCTYPE html>
<html lang="en">
<head>
<meta charset="UTF-8">
<title>Velo Grassworks — Lawn &amp; Landscape Flyer</title>
<link href="https://fonts.googleapis.com/css2?family=Poppins:wght@400;500;600;700;800&family=Montserrat:wght@800;900&display=swap" rel="stylesheet">
<style>
:root{
  --green-dark:#1e4d25;
  --green-deep:#0e5a25;
  --green:#169a3e;
  --green-bright:#1f9c3c;
  --lime:#8fd61c;
  --red:#e1141b;
  --yellow:#f5f000;
  --grey-panel:#e8e8e8;
  --ink:#1c1c1c;
  --white:#ffffff;
  --page:#d0d0d0;
}
*{margin:0;padding:0;box-sizing:border-box}
html,body{width:1200px;height:1200px;overflow:hidden;background:var(--page);font-family:'Poppins',sans-serif}
.flyer-wrap{position:absolute;left:150px;top:18px;width:900px;height:1164px}
.flyer{position:absolute;left:0;top:0;width:1314px;height:1700px;background:var(--white);transform:scale(.685);transform-origin:0 0;overflow:hidden;box-shadow:0 10px 30px rgba(0,0,0,.25)}
.abs{position:absolute;white-space:nowrap}

.brand-mark{left:87px;top:70px;width:400px;text-align:center}
.brand-mark .dot{width:70px;height:70px;border-radius:50%;background:var(--green);margin:0 auto 16px}
.brand-mark .name{font-weight:800;font-size:34px;color:var(--green-dark);letter-spacing:.5px;line-height:1}

.brand-line{left:87px;top:265px;font-size:33px;letter-spacing:5px;color:var(--ink);font-weight:400}
.brand-rule{left:87px;top:313px;width:448px;height:1px;background:#999}
.kicker{left:87px;top:326px;font-size:42px;font-weight:700;color:var(--green);letter-spacing:.5px}
.headline{left:84px;top:378px;font-family:'Montserrat',sans-serif;font-weight:900;font-size:82px;line-height:76px;color:var(--green-dark);letter-spacing:-2px}
.headline .experts{color:var(--green);letter-spacing:13px;font-size:56px;line-height:80px}
.steps{left:87px;top:602px;display:flex;gap:5px}
.steps span{width:16px;height:14px}
.subtitle{left:84px;top:628px;font-size:31px;line-height:36px;color:var(--ink);font-weight:500}

.photo{left:677px;top:0;width:553px;height:735px}

.why{left:83px;top:735px;width:1147px;height:202px;background:var(--grey-panel);border-radius:0 12px 12px 12px}
.why-tab{left:83px;top:735px}
.why-title{left:124px;top:748px;font-size:26px;font-weight:700;color:var(--white)}
.why-list{font-size:24px;color:var(--ink);display:flex;align-items:center;gap:12px}

.tick{width:14px;height:14px;border-radius:50%;background:var(--green);display:inline-block;position:relative;flex:none}
.tick::after{content:"";position:absolute;left:4px;top:3px;width:4px;height:6px;border:solid #fff;border-width:0 2px 2px 0;transform:rotate(45deg)}

.services-title{left:87px;top:967px;font-size:29px;color:var(--ink)}
.services-title b{color:var(--green-dark);font-weight:700}
.svc{font-size:21.5px;font-weight:500;color:var(--ink);display:flex;align-items:center;gap:12px}

.seasonal{left:881px;top:935px;width:349px;height:485px;background:var(--green-dark);border-radius:0 0 0 36px}
.seasonal-h1{left:38px;top:28px;font-size:33px;letter-spacing:7px;color:var(--white)}
.seasonal-h2{left:38px;top:62px;font-size:36px;font-weight:700;color:var(--green-bright)}
.seasonal-rule{left:38px;top:130px;width:45px;height:3px;background:var(--green-bright)}
.ss{font-size:21px;color:var(--white);display:flex;align-items:center;gap:12px;left:38px}

.offer-tab{height:56px;background:var(--red);border-radius:16px 16px 0 0;color:var(--white);font-weight:700;font-size:21px;text-align:center}
.offer{width:355px;height:197px;background:var(--green);border-radius:26px;overflow:hidden}
.offer .strip{position:absolute;left:0;bottom:0;width:100%;height:64px;background:#0f8a33}
.big{font-family:'Montserrat',sans-serif;font-weight:800;color:var(--white)}

.contact-title{left:89px;top:1468px;font-size:29px;font-weight:700;color:var(--green-dark)}
.contact-title span{color:var(--green)}
.tagline{left:556px;top:1462px;font-size:23px;font-weight:700;color:var(--ink)}
.pill{left:548px;top:1508px;width:685px;height:62px;border-radius:31px;background:var(--green-dark);overflow:hidden}
.pill .lead{position:absolute;left:0;top:0;width:250px;height:62px;background:var(--lime);border-radius:31px 0 0 31px;font-size:27px;font-weight:700;letter-spacing:3px;color:var(--green-dark);line-height:62px;padding-left:33px}
.pill .cap{position:absolute;left:212px;top:0;width:60px;height:62px;background:var(--green-dark);border-radius:31px 0 0 31px}
.pill .url{position:absolute;left:262px;top:0;font-size:27px;font-weight:700;color:var(--white);line-height:60px;white-space:nowrap}
.phone{left:90px;top:1558px;display:flex;align-items:center;gap:8px;font-size:47px;font-weight:700;color:var(--white)}
.phone .ic{width:38px;height:38px;border-radius:50%;background:var(--green)}
</style>
</head>
<body>
<div class="flyer-wrap">
<div class="flyer">

  <div class="abs brand-mark">
    <div class="dot"></div>
    <div class="name">VELO GRASSWORKS</div>
  </div>

  <div class="abs brand-line">VELO GRASSWORKS</div>
  <div class="abs brand-rule"></div>
  <div class="abs kicker">YOUR TRUSTED LOCAL</div>
  <div class="abs headline">LAWN &amp;<br>LANDSCAPE<br><span class="experts">EXPERTS</span></div>
  <div class="abs steps">
    <span style="background:#1e4d25"></span><span style="background:#3c6a42"></span><span style="background:#5f8764"></span><span style="background:#86a68a"></span><span style="background:#adc4af"></span><span style="background:#d3e0d4"></span>
  </div>
  <div class="abs subtitle">Providing Top-Tier Lawn Care and<br>Landscape Solutions for Every Season</div>

  <svg class="abs photo" viewBox="0 0 553 735">
    <defs>
      <linearGradient id="photoFill" x1="0" y1="0" x2="0" y2="1">
        <stop offset="0" stop-color="#b8c9a8"/>
        <stop offset=".35" stop-color="#6f9a4a"/>
        <stop offset="1" stop-color="#3f9a2a"/>
      </linearGradient>
    </defs>
    <rect x="0" y="450" width="553" height="285" fill="#1f8a34"/>
    <rect x="22" y="480" width="509" height="255" fill="#2e9c30"/>
    <path d="M0 0 H553 V420 Q553 480 500 525 L340 630 Q293 660 245 630 L55 520 Q0 485 0 420 Z" fill="url(#photoFill)" role="img" aria-label="Photo of a gardener pushing a lawn mower across a freshly cut lawn beside a brick house"/>
    <path d="M18 0 V405 Q18 465 70 500 L250 605 Q293 630 336 605 L480 515 Q535 480 535 410 V0" fill="none" stroke="#fff" stroke-width="4"/>
    <path d="M22 480 V735 M531 490 V735" stroke="#3dbb4d" stroke-width="4"/>
  </svg>

  <div class="abs why"></div>
  <svg class="abs why-tab" width="620" height="64" viewBox="0 0 620 64"><path d="M0 12 Q0 0 12 0 H620 Q595 12 580 40 Q565 64 525 64 H0 Z" fill="#1e4d25"/></svg>
  <div class="abs why-title">WHY CHOOSE VELO GRASSWORKS?</div>
  <div class="abs why-list" style="left:128px;top:812px"><i class="tick"></i>Reliable, Professional Service</div>
  <div class="abs why-list" style="left:128px;top:869px"><i class="tick"></i>Custom Lawn &amp; Landscape Plans</div>
  <div class="abs why-list" style="left:624px;top:812px"><i class="tick"></i>Licensed &amp; Insured for Your Peace of Mind</div>
  <div class="abs why-list" style="left:624px;top:869px"><i class="tick"></i>Satisfaction Guaranteed</div>

  <div class="abs services-title">OUR <b>SERVICES</b></div>
  <div class="abs svc" style="left:92px;top:1008px"><i class="tick"></i>Lawn Care &amp; Maintenance</div>
  <div class="abs svc" style="left:92px;top:1044px"><i class="tick"></i>Regular Mowing</div>
  <div class="abs svc" style="left:92px;top:1080px"><i class="tick"></i>Fertilization &amp; Weed Control</div>
  <div class="abs svc" style="left:92px;top:1116px"><i class="tick"></i>Aeration &amp; Overseeding</div>
  <div class="abs svc" style="left:487px;top:1008px"><i class="tick"></i>Landscape &amp; Garden Solutions</div>
  <div class="abs svc" style="left:487px;top:1044px"><i class="tick"></i>Mulching &amp; Bed Maintenance</div>
  <div class="abs svc" style="left:487px;top:1080px"><i class="tick"></i>Planting &amp; Pruning</div>
  <div class="abs svc" style="left:487px;top:1116px"><i class="tick"></i>Sod Installation</div>

  <div class="abs seasonal">
    <div class="abs seasonal-h1">SEASONAL</div>
    <div class="abs seasonal-h2">SERVICES</div>
    <div class="abs seasonal-rule"></div>
    <div class="abs ss" style="top:172px"><i class="tick"></i>Leaf &amp; Debris Clean-up</div>
    <div class="abs ss" style="top:213px"><i class="tick"></i>Snow &amp; Ice Removal</div>
    <div class="abs ss" style="top:254px"><i class="tick"></i>Spring/Fall Clean-ups</div>
    <div class="abs ss" style="top:295px"><i class="tick"></i>Hardscaping Projects</div>
    <div class="abs ss" style="top:336px"><i class="tick"></i>Patios &amp; Walkways</div>
    <div class="abs ss" style="top:377px"><i class="tick"></i>Retaining Walls</div>
    <div class="abs ss" style="top:418px"><i class="tick"></i>Outdoor Living Spaces</div>
  </div>

  <div class="abs offer-tab" style="left:170px;top:1180px;width:205px;line-height:56px">SPECIAL OFFER</div>
  <div class="abs offer" style="left:95px;top:1228px">
    <div class="abs big" style="left:24px;top:34px;font-size:68px;line-height:1;letter-spacing:-2px">20</div>
    <div class="abs big" style="left:106px;top:30px;font-size:44px;line-height:1">%</div>
    <div class="abs" style="left:106px;top:78px;font-size:24px;color:#fff">OFF</div>
    <div class="abs" style="left:167px;top:30px;font-size:23px;font-weight:800;line-height:26px;color:#fff">YOUR FIRST<br>LAWN CARE<br>SERVICE!</div>
    <div class="strip"></div>
    <div class="abs" style="left:40px;top:138px;font-size:16px;line-height:20px;color:#fff">Call or text today<br>to schedule your</div>
    <div class="abs" style="left:197px;top:138px;font-size:15px;font-weight:700;line-height:20px;color:var(--yellow)">FREE<br>CONSULTATION.</div>
  </div>

  <div class="abs offer-tab" style="left:546px;top:1180px;width:205px;padding-top:4px;line-height:24px">
    <div style="font-size:18px;font-style:italic;font-weight:500">Winter</div>SPECIAL OFFER</div>
  <div class="abs offer" style="left:471px;top:1228px">
    <div class="abs big" style="left:26px;top:34px;font-size:22px">$</div>
    <div class="abs big" style="left:41px;top:32px;font-size:60px;line-height:1;letter-spacing:-2px">100</div>
    <div class="abs" style="left:124px;top:80px;font-size:18px;color:#fff">OFF</div>
    <div class="abs" style="left:170px;top:34px;font-size:18px;font-weight:800;line-height:22px;color:#fff">SNOW REMOVAL<br>SERVICE</div>
    <div class="abs" style="left:170px;top:80px;font-size:17px;color:#fff">(TILL 06.05.2025)</div>
    <div class="strip"></div>
    <div class="abs" style="left:24px;top:140px;font-size:12px;line-height:16px;color:#fff">Fall Clean-Up Special:<br>Free Leaf Removal with<br>Any Lawn Care Package</div>
    <div class="abs" style="left:204px;top:140px;font-size:12px;font-weight:700;line-height:16px;color:var(--yellow)">Summer Ready:<br>10% Off Mulch<br>installation</div>
  </div>

  <div class="abs contact-title">CONTACT <span>US TODAY!</span></div>
  <div class="abs tagline">Let’s make your lawn the envy of the neighborhood!</div>

  <svg class="abs" style="left:0;top:1440px" width="1314" height="260" viewBox="0 0 1314 260">
    <defs>
      <linearGradient id="grassFill" x1="0" y1="0" x2="0" y2="1">
        <stop offset="0" stop-color="#ffffff" stop-opacity="0"/>
        <stop offset=".5" stop-color="#b9e06a"/>
        <stop offset="1" stop-color="#5fae2a"/>
      </linearGradient>
    </defs>
    <rect x="560" y="80" width="754" height="180" fill="url(#grassFill)" role="img" aria-label="Fresh green grass blades along the bottom edge"/>
    <path d="M0 70 H360 Q470 70 530 150 Q590 240 720 250 H1314 V260 H0 Z" fill="#0e5a25"/>
  </svg>

  <div class="abs pill">
    <div class="lead">Visit us at</div>
    <div class="cap"></div>
    <div class="url">www.velograssworks.com</div>
  </div>

  <div class="abs phone">
    <svg class="ic" viewBox="0 0 38 38"><circle cx="19" cy="19" r="19" fill="#169a3e"/><path d="M13 10 L16 10 L17.5 15 L15.5 16.5 Q17 20.5 21.5 22.5 L23 20.5 L28 22 L28 25 Q27 28 24 28 Q11 27 10 14 Q10 11 13 10 Z" fill="#fff"/></svg>
    555 0142 7788
  </div>

</div>
</div>
</body>
</html>
```